Business card design for Allied Healthcare provider

We would like a design for front and back of business cards. The design must resonate with all levels of customers from patients, to other health providers and medical. Must also resonate with corporate customers

Target Market(s)

patients, medical practitioners, other health providers and corporate.

Industry/Entity Type

healthcare

Contact Information for Business Card

name, logo, phone and fax numbers, email, website

Requirements
Must have
• not allowing me to change this, but the card must be double sided!! Please take note
Nice to have
• a fresh yet bold design to catch attention.

```html
<!DOCTYPE html>
<html lang="en">
<head>
<meta charset="utf-8">
<title>carevale business card – front and back</title>
<link href="https://fonts.googleapis.com/css2?family=Montserrat:wght@500;600;700;800&display=swap" rel="stylesheet">
<style>
  :root {
    --navy: #182b57;
    --gold: #f7b82b;
    --white: #ffffff;
    --stage: #1c1c1f;
    --ink: #10183a;
  }
  * { box-sizing: border-box; margin: 0; padding: 0; }
  html, body { width: 1200px; height: 900px; overflow: hidden; }
  body {
    background: var(--stage);
    font-family: "Montserrat", sans-serif;
    position: relative;
  }
  .card {
    position: absolute;
    left: 280px;
    width: 640px;
    height: 366px;
    border-radius: 26px;
    overflow: hidden;
  }
  .card--front { top: 60px; background: var(--white); }
  .card--back { top: 474px; background: var(--navy); }

  .card__sides { position: absolute; inset: 0; width: 100%; height: 100%; }

  .brand {
    position: absolute;
    display: flex;
    align-items: center;
    gap: 12px;
    font-weight: 700;
    letter-spacing: 0.5px;
  }
  .brand__dot { border-radius: 50%; background: var(--gold); flex: none; }

  .card--front .brand {
    top: 78px; left: 50%; transform: translateX(-50%);
    color: var(--navy); font-size: 44px;
  }
  .card--front .brand__dot { width: 22px; height: 22px; }

  .card--back .brand {
    top: 50%; left: 50%; transform: translate(-50%, -50%);
    color: var(--white); font-size: 58px;
  }
  .card--back .brand__dot { width: 28px; height: 28px; }

  .identity {
    position: absolute;
    top: 170px; right: 335px;
    text-align: right;
    color: var(--ink);
  }
  .identity__name {
    font-weight: 800; font-size: 17px; color: var(--navy);
    text-transform: uppercase; letter-spacing: 0.3px;
  }
  .identity__role { font-weight: 500; font-size: 14px; margin-top: 3px; }
  .identity__address { font-weight: 500; font-size: 13.5px; margin-top: 12px; line-height: 1.45; }

  .divider {
    position: absolute;
    top: 175px; left: 320px;
    width: 2px; height: 122px;
    background: var(--navy);
  }

  .contacts {
    position: absolute;
    top: 178px; left: 338px;
    list-style: none;
    color: var(--ink);
    font-weight: 500; font-size: 14px;
  }
  .contacts__item { display: flex; align-items: center; gap: 10px; height: 29px; }
  .contacts__icon { width: 16px; height: 16px; fill: var(--navy); flex: none; }
</style>
</head>
<body>

<section class="card card--front" aria-label="Card front">
  <svg class="card__sides" viewBox="0 0 640 366" aria-hidden="true">
    <path d="M0 0 H95 Q10 183 95 366 H0 Z" fill="var(--navy)"/>
    <path d="M95 0 Q10 183 95 366" fill="none" stroke="var(--gold)" stroke-width="7" transform="translate(8 0)"/>
    <path d="M640 0 H545 Q630 183 545 366 H640 Z" fill="var(--navy)"/>
    <path d="M545 0 Q630 183 545 366" fill="none" stroke="var(--gold)" stroke-width="7" transform="translate(-8 0)"/>
  </svg>

  <div class="brand"><span class="brand__dot"></span><span class="brand__name">carevale</span></div>

  <div class="identity">
    <p class="identity__name">Nora Whitfield</p>
    <p class="identity__role">Co-Founder</p>
    <p class="identity__address">418 N. Harbor Lane<br>Suite 210 Eastfield.14</p>
  </div>

  <div class="divider"></div>

  <ul class="contacts">
    <li class="contacts__item">
      <svg class="contacts__icon" viewBox="0 0 16 16" aria-hidden="true"><path d="M3.5 1.5l2.3 2.8-1.3 1.6c.8 1.9 2.4 3.5 4.3 4.3l1.6-1.3 2.8 2.3-1.2 2.3C7.5 13.7 2.3 8.5 1.2 3z"/></svg>
      <span>555-240-1187</span>
    </li>
    <li class="contacts__item">
      <svg class="contacts__icon" viewBox="0 0 16 16" aria-hidden="true"><path d="M4 1h8v4H4zM1 6h14v6h-3v3H4v-3H1zM5 10v4h6v-4z"/></svg>
      <span>555-240-119</span>
    </li>
    <li class="contacts__item">
      <svg class="contacts__icon" viewBox="0 0 16 16" aria-hidden="true"><path d="M1 3h14v10H1zM2.5 4.5L8 9l5.5-4.5z" fill-rule="evenodd"/></svg>
      <span>info@carevale.com</span>
    </li>
    <li class="contacts__item">
      <svg class="contacts__icon" viewBox="0 0 16 16" aria-hidden="true"><circle cx="8" cy="8" r="7"/><path d="M1 8h14M8 1c-3 3.5-3 10.5 0 14M8 1c3 3.5 3 10.5 0 14" stroke="#fff" stroke-width="1" fill="none"/></svg>
      <span>www.carevale.com</span>
    </li>
  </ul>
</section>

<section class="card card--back" aria-label="Card back">
  <div class="brand"><span class="brand__dot"></span><span class="brand__name">carevale</span></div>
</section>

</body>
</html>
```